Website for software company "velbra"

We need a website for our software company/startup named "velbra". We are developing several products (currently 3 standard-software products) which are all in different sectors, but all our products are available for Laptops/PC/Mobile Phones/Tablets, ... We do also create custom software and support our customers with consulting to optimize their processes.
We already have a Logo which you can find in the attached files.
We are a young team of 4 members (two founders and 2 employees).

To get an idea of our products -> the first one is a planning software for healthcare organizations (eg. Mercyway, firebrigade, pharmacy), the second one is a booking software for sport clubs and the third one is a competition software for sports hunting. You see very diverse. Include or ignore this info of our products as you like.

The design has to be a bootstrap 4 (or higher) design. We have licenced FontAwesome as iconset. Responsive design should come without saying.

Coding

Coded - Design and coding required

Number of Pages Required

5+ page

Font styles to use
Sans Serif

Requirements
Must have
• Starting page, product pages, news section, contact, team, services

```html
<!DOCTYPE html>
<html lang="en">
<head>
<meta charset="utf-8">
<title>Velbra Software</title>
<link rel="stylesheet" href="https://fonts.googleapis.com/css2?family=Poppins:wght@400;500;600;700;800&family=Alegreya:wght@700&display=swap">
<style>
:root{
  --orange:#f5812f;
  --orange-dark:#e5701f;
  --black:#000;
  --panel:#333333;
  --white:#fff;
  --ink:#111;
}
*{box-sizing:border-box;margin:0;padding:0}
html,body{width:1200px;height:3025px;overflow:hidden;background:var(--black);font-family:'Poppins',sans-serif;color:var(--white)}
.page{position:relative;width:1200px;height:3025px;overflow:hidden}
.abs{position:absolute}
.photo{position:absolute}
.hero-photo{left:0;top:0;width:1200px;height:784px;background:linear-gradient(120deg,#5c6e7a 0%,#c9d2d6 30%,#3a4650 55%,#1e2a33 80%,#55606a 100%)}
.topbar{left:517px;top:0;width:683px;height:49px;background:var(--orange);clip-path:polygon(0 0,100% 0,100% 100%,40px 100%)}
.topbar span{position:absolute;top:16px;font-size:13px;color:var(--white);white-space:nowrap}
.navbar{left:517px;top:49px;width:683px;height:51px;background:var(--white);clip-path:polygon(40px 0,100% 0,100% 100%,0 100%)}
.navbar a{position:absolute;top:17px;font-size:13px;font-weight:600;color:var(--ink);text-decoration:none}
.brand{left:96px;top:22px;font-size:56px;font-weight:700;color:var(--orange);letter-spacing:1px;display:flex;align-items:center;gap:12px}
.brand i{display:block;width:22px;height:22px;background:var(--orange);border-radius:50%}
.hero-box{left:161px;top:223px;width:878px;height:329px;background:rgba(40,40,40,.72);text-align:center}
.hero-welcome{position:absolute;left:0;right:0;top:48px;font-family:'Alegreya',serif;font-size:31px;font-weight:700}
.hero-title{position:absolute;left:0;right:0;top:86px;font-size:64px;font-weight:700;letter-spacing:1px}
.hero-text{position:absolute;left:120px;right:120px;top:176px;font-size:13px;line-height:21px}
.btn{position:absolute;background:var(--orange);color:var(--white);font-weight:600;font-size:15px;display:flex;align-items:center;justify-content:center}
.dots span{position:absolute;left:1100px;width:12px;height:12px;border:1.5px solid var(--orange);border-radius:50%}
.sectors{left:160px;top:680px;width:879px;height:386px;background:var(--panel)}
.sector{top:700px;width:269px;height:347px}
.sector-label{position:absolute;left:12px;bottom:17px;width:237px;height:53px;background:var(--panel);color:var(--orange);font-weight:700;font-size:18px;display:flex;align-items:center;justify-content:center}
.about-frame{left:101px;top:1150px;width:539px;height:429px;background:var(--panel);padding:7px}
.about-photo{width:100%;height:100%;background:linear-gradient(135deg,#a9b3b8,#e7ebec 40%,#57626a 75%,#2b3238)}
h2{font-weight:700;font-size:34px}
h2 em{font-style:normal;color:var(--orange)}
.about-title{left:675px;top:1170px}
.about-text{left:675px;top:1224px;width:430px;font-size:12px;line-height:20px}
.about-text p+p{margin-top:20px}
.device{top:1494px;width:175px;height:113px;background:var(--panel);border-radius:4px;text-align:center}
.device svg{position:absolute;left:50%;top:12px;transform:translateX(-50%)}
.device b{position:absolute;left:0;right:0;bottom:12px;font-size:15px;font-weight:600}
.clients{left:0;top:1720px;width:1200px;height:570px;background:var(--orange)}
.center{left:0;width:1200px;text-align:center}
.lead{font-size:13px;line-height:21px}
.card{top:1912px;width:426px;height:206px;background:var(--white);border-radius:6px;color:#555;padding:26px 28px}
.card p{font-size:11.5px;line-height:19px}
.avatar{position:absolute;left:28px;top:113px;width:62px;height:62px;border-radius:50%;background:linear-gradient(180deg,#6d88c9,#c9d5ef)}
.card .name{position:absolute;left:104px;top:122px;color:var(--orange);font-weight:600;font-size:16px}
.card .role{position:absolute;left:104px;top:146px;font-size:12px;color:#222}
.contact-item{left:130px;width:300px;height:51px}
.contact-item .ico{position:absolute;left:0;top:0;width:51px;height:51px;border:2px solid var(--white);background:var(--orange);display:flex;align-items:center;justify-content:center}
.contact-item .txt{position:absolute;left:68px;top:4px;font-size:12.5px;line-height:18px;white-space:nowrap}
.contact-item .txt b{font-size:15px;font-weight:600;display:block}
.field{left:486px;width:283px;height:49px;border:1.5px solid var(--white);font-size:12.5px;padding:14px 24px}
.footer-links a{position:absolute;top:2918px;font-size:15px;color:var(--white);text-decoration:none}
.social-sq{position:absolute;top:2980px;width:22px;height:22px;border:2.5px solid var(--white);border-radius:5px}
</style>
</head>
<body>
<div class="page">

  <div class="photo hero-photo" role="img" aria-label="Developers working together at computer screens showing code"></div>

  <div class="abs topbar">
    <span style="left:52px">☎ +0 555 010 2233</span>
    <span style="left:213px">✉ info@velbra.com</span>
    <span style="left:383px">◯ Login Here</span>
    <span style="left:506px;top:15px;width:19px;height:19px;border-radius:50%;background:var(--white)"></span>
    <span style="left:534px;top:15px;width:19px;height:19px;border-radius:50%;background:var(--white)"></span>
    <span style="left:562px;top:15px;width:19px;height:19px;border-radius:50%;background:var(--white)"></span>
  </div>
  <nav class="abs navbar">
    <a style="left:51px">HOME</a>
    <a style="left:130px">ABOUT US</a>
    <a style="left:237px">OUR SERVICES</a>
    <a style="left:372px">SHOP</a>
    <a style="left:448px">FAQ</a>
    <a style="left:514px">CONTACT</a>
  </nav>

  <div class="abs brand"><i></i>VELBRA</div>

  <div class="abs hero-box">
    <div class="hero-welcome">welcome to</div>
    <div class="hero-title">VELBRA SOFTWARE</div>
    <div class="hero-text">Lorem ipsum dolor sit amet, consectetur adipiscing elit, sed do eiusmod tempor incididunt ut labore et dolore magna aliqua. Quis ipsum suspendisse ultrices gravida.</div>
    <div class="btn" style="left:368px;top:234px;width:144px;height:42px">GET STARTED</div>
  </div>
  <div class="dots">
    <span style="top:356px;background:var(--orange)"></span>
    <span style="top:374px"></span><span style="top:392px"></span><span style="top:410px"></span>
  </div>

  <div class="abs sectors"></div>
  <div class="photo sector" style="left:181px;background:linear-gradient(160deg,#d9eefa,#5aa5cf 60%,#2a5f86)" role="img" aria-label="Hospital operating room">
    <div class="sector-label">HEALTHCARE</div></div>
  <div class="photo sector" style="left:466px;background:linear-gradient(160deg,#7d6a4a,#b8302a 50%,#6b1d18)" role="img" aria-label="Young football players celebrating">
    <div class="sector-label">SPORT CLUBS</div></div>
  <div class="photo sector" style="left:751px;background:linear-gradient(160deg,#4f5a3a,#7b6a45 50%,#3a3a3a)" role="img" aria-label="Shooter at an outdoor hunting range">
    <div class="sector-label">SPORTS HUNTING</div></div>

  <div class="abs about-frame"><div class="about-photo" role="img" aria-label="Team collaborating at computers in an office"></div></div>
  <h2 class="abs about-title">ABOUT <em>US</em></h2>
  <div class="abs about-text">
    <p>Lorem ipsum dolor sit amet, consectetur adipiscing elit, sed do eiusmod tempor incididunt ut labore et dolore magna aliqua. Quis ipsum suspendisse ultrices gravida. Risus commodo viverra maecenas accumsan lacus vel facilisis.</p>
    <p>Lorem ipsum dolor sit amet, consectetur adipiscing elit, sed do eiusmod tempor incididunt ut labore et dolore magna aliqua. Quis ipsum suspendisse ultrices gravida. Risus commodo</p>
  </div>
  <div class="btn" style="left:675px;top:1409px;width:143px;height:44px">READ MORE</div>

  <div class="abs device" style="left:318px">
    <svg width="84" height="56" viewBox="0 0 84 56" fill="none" stroke="#f5812f" stroke-width="2.5"><rect x="10" y="3" width="64" height="42"/><path d="M2 52h80"/></svg>
    <b>LAPTOPS</b></div>
  <div class="abs device" style="left:512px">
    <svg width="66" height="56" viewBox="0 0 66 56" fill="none" stroke="#f5812f" stroke-width="2.5"><rect x="3" y="3" width="60" height="40" rx="2"/><path d="M3 36h60M33 43v8M20 53h26"/></svg>
    <b>PC</b></div>
  <div class="abs device" style="left:706px">
    <svg width="56" height="56" viewBox="0 0 56 56" fill="none" stroke="#f5812f" stroke-width="2"><rect x="16" y="3" width="26" height="50" rx="4"/><circle cx="38" cy="28" r="7"/><rect x="10" y="18" width="12" height="9"/><circle cx="6" cy="40" r="2"/><circle cx="50" cy="12" r="2"/></svg>
    <b>MOBILE PHONES</b></div>
  <div class="abs device" style="left:899px">
    <svg width="44" height="56" viewBox="0 0 44 56" fill="none" stroke="#f5812f" stroke-width="2.5"><rect x="4" y="3" width="36" height="50" rx="4"/><path d="M4 11h36M4 45h36"/></svg>
    <b>TABLETS</b></div>

  <div class="abs clients" role="img" aria-label="Orange toned background of a modern living space"></div>
  <svg class="abs" style="left:0;top:2200px" width="1200" height="92" viewBox="0 0 1200 92"><polygon points="0,90 600,1 1200,90 1200,92 0,92" fill="#000"/></svg>
  <h2 class="abs center" style="top:1788px">HAPPY CLIENTS SAYS</h2>
  <div class="abs center lead" style="top:1842px"><div style="width:660px;margin:0 auto">Lorem ipsum dolor sit amet, consectetur adipiscing elit, sed do eiusmod tempor incididunt ut labore et dolore magna aliqua. Quis ipsum suspendisse ultrices gravida.</div></div>
  <svg class="abs" style="left:97px;top:1990px" width="20" height="30" viewBox="0 0 20 30"><path d="M16 3L4 15l12 12" stroke="#fff" stroke-width="3" fill="none"/></svg>
  <svg class="abs" style="left:1083px;top:1990px" width="20" height="30" viewBox="0 0 20 30"><path d="M4 3l12 12L4 27" stroke="#fff" stroke-width="3" fill="none"/></svg>
  <div class="abs card" style="left:161px">
    <p>“ Lorem ipsum dolor sit amet, consectetur adipiscing elit, sed do eiusmod tempor incididunt ut labore et dolore magna aliqua. Quis ipsum suspendisse ultrices gravida. Risus commodo viverra maecenas accumsan lacus vel facilisis.......”</p>
    <div class="avatar" role="img" aria-label="Client portrait"></div>
    <div class="name">Elena Marsh</div><div class="role">Position Name</div>
  </div>
  <div class="abs card" style="left:613px">
    <p>“ Lorem ipsum dolor sit amet, consectetur adipiscing elit, sed do eiusmod tempor incididunt ut labore et dolore magna aliqua. Quis ipsum suspendisse ultrices gravida. Risus commodo viverra maecenas accumsan lacus vel facilisis.......”</p>
    <div class="avatar" style="background:linear-gradient(180deg,#9cc79a,#e3efe0)" role="img" aria-label="Client portrait"></div>
    <div class="name">Nadia Fenwick</div><div class="role">Position Name</div>
  </div>

  <h2 class="abs center" style="top:2285px">GET IN <em>TOUCH</em></h2>
  <div class="abs center lead" style="top:2346px"><div style="width:660px;margin:0 auto">Lorem ipsum dolor sit amet, consectetur adipiscing elit, sed do eiusmod tempor incididunt ut labore et dolore magna aliqua. Quis ipsum suspendisse ultrices gravida.</div></div>

  <div class="abs contact-item" style="top:2421px">
    <div class="ico"><svg width="20" height="26" viewBox="0 0 20 26"><path d="M10 1C5 1 1 5 1 10c0 7 9 15 9 15s9-8 9-15c0-5-4-9-9-9z" fill="#fff"/><circle cx="10" cy="10" r="3.5" fill="#f5812f"/></svg></div>
    <div class="txt">18 Harbor Lane, Westfield Park,<br>Northvale - 40219</div></div>
  <div class="abs contact-item" style="top:2489px">
    <div class="ico"><svg width="22" height="22" viewBox="0 0 22 22"><path d="M5 1l4 5-2 3c1 3 3 5 6 6l3-2 5 4-3 4C9 21 1 13 1 4z" fill="#fff"/></svg></div>
    <div class="txt"><b>CALL ON</b>+0 555 010 4471</div></div>
  <div class="abs contact-item" style="top:2558px">
    <div class="ico"><svg width="24" height="18" viewBox="0 0 24 18" fill="none" stroke="#fff" stroke-width="2"><rect x="1" y="1" width="22" height="16"/><path d="M1 1l11 9 11-9"/></svg></div>
    <div class="txt"><b>EMAIL AT</b>info@velbra.com</div></div>
  <div class="abs contact-item" style="top:2627px">
    <div class="ico"><svg width="24" height="24" viewBox="0 0 24 24" fill="none" stroke="#fff" stroke-width="1.8"><circle cx="12" cy="12" r="10"/><ellipse cx="12" cy="12" rx="4.5" ry="10"/><path d="M2 12h20M4 6h16M4 18h16"/></svg></div>
    <div class="txt"><b>VISIT US</b>www.velbra.com</div></div>

  <div class="abs field" style="top:2428px">First Name</div>
  <div class="abs field" style="top:2491px">Last Name</div>
  <div class="abs field" style="top:2555px">Phone Number</div>
  <div class="abs field" style="top:2618px">Email Address</div>
  <div class="abs field" style="left:787px;top:2428px;height:176px">Your Message Goes Here.........</div>
  <div class="btn" style="left:787px;top:2618px;width:283px;height:49px">SUBMIT NOW</div>

  <div class="abs" style="left:0;top:2745px;width:1200px;height:280px;background:var(--orange)" role="img" aria-label="Orange toned background of house rooftops"></div>
  <svg class="abs" style="left:0;top:2745px" width="1200" height="92" viewBox="0 0 1200 92"><polygon points="0,0 1200,0 1200,2 600,90 0,2" fill="#000"/></svg>

  <h2 class="abs" style="left:101px;top:2862px;font-size:24px;font-weight:600">QUICK LINKS</h2>
  <div class="footer-links">
    <a style="left:101px">HOME</a><a style="left:207px">ABOUT US</a><a style="left:344px">OUR SERVICES</a><a style="left:515px">GALLERY</a><a style="left:640px">CONTACT US</a>
  </div>
  <div class="abs" style="left:101px;top:2958px;font-size:13px">Copyright © 2022 Velbra Software . All Rights Reserved.</div>

  <h2 class="abs" style="left:832px;top:2862px;font-size:24px;font-weight:600">JOIN WITH US</h2>
  <div class="abs" style="left:832px;top:2914px;width:269px;height:40px;background:var(--white);border:2px solid var(--white)">
    <span style="position:absolute;left:16px;top:10px;font-size:12.5px;color:var(--ink)">Email Address</span>
    <span style="position:absolute;right:0;top:0;width:108px;height:36px;background:var(--orange);font-weight:600;font-size:15px;display:flex;align-items:center;justify-content:center">SUBSCRIBE</span>
  </div>
  <span class="social-sq" style="left:968px"></span>
  <span class="social-sq" style="left:1006px"></span>
  <span class="social-sq" style="left:1043px"></span>
  <span class="social-sq" style="left:1081px"></span>
</div>
</body>
</html>
```